Varnel Flyer

We need a flyer designed for a Security Company. Our main focus is security consulting and risk management. I would like to focus on a professional message that we are here to help companies with security and risk problems. We are independent and do not affiliate with any other companies.

Who we are:
Over 25+ years of experience in Security and Law Enforcement
Specialize in Security Management
Board Certified in Security management
Accredited defense Specialist (ADS)
We are not affiliated with any security provider or guard company we provide independent advise

Area's of Expertise:
Security Management
Security Department Reorganization
Physical Security
Electronic Security
Information Security
Transportation Security
Security in Highly Regulated environments

Services Offered:

Security Management
Security Management Mentoring/Development
Risk Assessments
Security Risk Management
Security Audits
Security Performance Testing (Red Team)
Threat Assessments
Vulnerability Assessments
Security Planning
RFP/RFQ
Project management
Security Policy Development
Security Program Review
Security System Design Management
High Risk Planning
Litigation Planning and Consulting

What to look for in a Security Consultant:

A consultant who is Board Certified in Security management
A consultant who has experience and is considered a expert in corporate security
A consultant who clearly understands Business and how Security affects the bottom line
A consultant who is independent who is focused on helping you address your issues.
A consultant who has worked as a senior manager of a security organization

Industries:

Energy
Healthcare
Real Estate
Nuclear
Highly secure facilities

Accredited Defense Specialist (ADS)

The Accredited Defense Specialist (ADSⓇ) is considered the “gold standard” certification for security management professionals and demonstrates knowledge and competency in seven key domains of security. Globally recognized as the standard of excellence for security management professionals. The ADS is administered by OPRA Worldwide, which is the predominant international organization for security Internationally.

Contact us:

Phone: 555-271-6043
info@varnelguard.example
www.varnelguard.example

```html
<!DOCTYPE html>
<html lang="en">
<head>
<meta charset="utf-8">
<title>Varnel Flyer</title>
<link rel="stylesheet" href="https://fonts.googleapis.com/css2?family=Lato:wght@400;700;900&family=Roboto+Condensed:wght@700&display=swap">
<style>
:root{
  --backdrop:#5b5b5b;
  --paper:#ffffff;
  --brand-blue:#1f4f9e;
  --deep-blue:#173f85;
  --slate:#4a4a4d;
  --charcoal:#38383a;
  --ink:#2b2b2b;
  --muted:#6d7480;
}
*{margin:0;padding:0;box-sizing:border-box}
html,body{width:1200px;height:900px;overflow:hidden}
body{background:var(--backdrop);font-family:"Lato",sans-serif;color:var(--ink);position:relative}
.page{position:absolute;top:82px;width:519px;height:734px;background:var(--paper);overflow:hidden}
.page--front{left:55px}
.page--back{left:624px}
.layer{position:absolute;left:0;top:0}
.brand{position:absolute;display:flex;align-items:center;gap:8px;color:var(--brand-blue);font-weight:900;letter-spacing:2px;text-transform:uppercase}
.brand__mark{width:18px;height:18px;background:var(--brand-blue)}
.cert-badge{position:absolute;background:var(--brand-blue);border-radius:6px}
ul{list-style:none}
.shield-list li{position:relative;padding-left:13px;font-size:10px;line-height:12.6px}
.shield-list li::before{content:"";position:absolute;left:0;top:2.5px;width:7px;height:8px;background:currentColor;opacity:.75;clip-path:polygon(50% 0,100% 15%,100% 55%,50% 100%,0 55%,0 15%)}
/* front page */
.consultant{position:absolute;left:32px;top:300px;width:470px;color:var(--ink)}
.section-title{color:var(--brand-blue);font-weight:700;font-size:11px;margin-bottom:8px}
.consultant li{color:#333}
.industries{position:absolute;left:0;top:398px;width:519px;height:156px;background:var(--brand-blue)}
.industries__title{position:absolute;left:141px;top:2px;width:240px;height:28px;background:var(--paper);clip-path:polygon(8% 0,100% 0,92% 100%,0 100%);font-family:"Roboto Condensed",sans-serif;font-weight:700;font-size:22px;color:var(--brand-blue);text-align:center;line-height:28px}
.industries__row{position:absolute;left:0;top:49px;width:519px;display:flex}
.industry{position:absolute;width:100px;margin-left:-50px;text-align:center;color:#fff;font-size:10.5px;font-weight:700;line-height:12.5px}
.industry svg{display:block;margin:0 auto 9px}
.certification{position:absolute;left:32px;top:563px;width:341px}
.certification p{font-size:10px;line-height:12.7px;text-align:justify;color:#333}
/* contact */
.contact-tab{position:absolute;left:0;top:668px;width:137px;height:25px;background:var(--brand-blue);clip-path:polygon(0 0,84% 0,100% 100%,0 100%)}
.contact-tab span{position:absolute;left:21px;top:4px;color:#fff;font-size:15px;font-weight:700;text-decoration:underline;text-underline-offset:3px}
.contact-bar{position:absolute;left:0;top:692px;width:519px;height:42px;background:var(--brand-blue);color:#fff}
.contact-bar .item{position:absolute;top:0;height:42px;display:flex;align-items:center;gap:12px}
.contact-bar .phone{left:26px;font-size:14.5px}
.contact-bar .mail{left:176px;font-size:10.5px}
.contact-bar .web{left:344px;font-size:10.5px}
.contact-bar .divider{position:absolute;top:10px;width:1px;height:24px;background:#fff}
/* back page */
.panel-tab{position:absolute;height:16px;background:var(--brand-blue);color:#fff;font-size:10px;font-weight:700;line-height:16px;padding-left:10px;clip-path:polygon(4% 0,100% 0,96% 100%,0 100%)}
.panel-tab::after{content:"";position:absolute;right:-1px;top:0;width:9px;height:16px;background:var(--paper);clip-path:polygon(60% 0,100% 0,40% 100%,0 100%)}
.who{position:absolute;left:16px;top:409px;width:246px;color:#fff}
.who li,.expertise li{color:#f1f1f1}
.expertise{position:absolute;left:16px;top:537px;width:246px}
.services-tab{position:absolute;left:320px;top:386px;width:110px;height:17px;background:var(--paper);color:var(--ink);font-size:10.5px;font-weight:700;line-height:17px;padding-left:10px;clip-path:polygon(3% 0,100% 0,97% 100%,0 100%)}
.services-tab::after{content:"";position:absolute;right:0;top:0;width:7px;height:17px;background:var(--charcoal);clip-path:polygon(50% 0,100% 0,50% 100%,0 100%)}
.services{position:absolute;left:230px;top:413px;width:289px;color:#fff}
.services__edge{float:left;width:96px;height:215px;shape-outside:polygon(0 0,95px 0,40px 215px,0 215px)}
.services li{font-size:10px;line-height:12.6px}
.services li::before{content:"";display:inline-block;width:7px;height:8px;margin-right:6px;background:#fff;opacity:.8;clip-path:polygon(50% 0,100% 15%,100% 55%,50% 100%,0 55%,0 15%)}
</style>
</head>
<body>

<!-- FRONT PAGE -->
<section class="page page--front">
  <svg class="layer" width="519" height="290" viewBox="0 0 519 290">
    <defs>
      <linearGradient id="cityGrad" x1="0" y1="0" x2="1" y2="1">
        <stop offset="0" stop-color="#6f8f99"/>
        <stop offset=".5" stop-color="#40565f"/>
        <stop offset="1" stop-color="#1f2c33"/>
      </linearGradient>
      <radialGradient id="dusk" cx=".12" cy=".8" r=".35">
        <stop offset="0" stop-color="#d9a46a" stop-opacity=".8"/>
        <stop offset="1" stop-color="#d9a46a" stop-opacity="0"/>
      </radialGradient>
    </defs>
    <polygon points="0,14 334,14 360,46 519,46 519,52 357,52 331,20 0,20" fill="var(--deep-blue)"/>
    <g role="img" aria-label="City skyline at dusk overlaid with glowing connected security icons">
      <polygon points="0,22 330,22 356,54 519,54 519,268 150,268 124,238 0,238" fill="url(#cityGrad)"/>
      <polygon points="0,22 330,22 356,54 519,54 519,268 150,268 124,238 0,238" fill="url(#dusk)"/>
    </g>
    <polygon points="40,240 126,240 152,270 519,270 519,276 148,276 122,246 46,246" fill="var(--slate)"/>
    <polygon points="160,279 519,279 519,282 160,282" fill="var(--brand-blue)"/>
  </svg>

  <div class="brand" style="left:24px;top:262px;font-size:20px">
    <span class="brand__mark"></span>Varnel
  </div>

  <div class="consultant">
    <h2 class="section-title">What to look for in a Security Consultant:</h2>
    <ul class="shield-list">
      <li>A consultant who is Board Certified in Security management</li>
      <li>A consultant who has experience and is considered a expert in corporate security</li>
      <li>A consultant who clearly understands Business and how Security affects the bottom line</li>
      <li>A consultant who is independent who is focused on helping you address your issues.</li>
      <li>A consultant who has worked as a senior manager of a security organization</li>
    </ul>
  </div>

  <div class="industries">
    <div class="industries__title">INDUSTRIES</div>
    <div class="industry" style="left:70px;top:49px">
      <svg width="68" height="68" viewBox="0 0 68 68" role="img" aria-label="Shield with power pylon icon"><path d="M34 2 L66 12 L64 40 Q58 58 34 66 Q10 58 4 40 L2 12 Z" fill="#fff"/><path d="M34 10 L58 17 L56 39 Q51 53 34 59 Q17 53 12 39 L10 17 Z" fill="var(--brand-blue)" opacity=".15"/></svg>
      Energy
    </div>
    <div class="industry" style="left:165px;top:49px">
      <svg width="68" height="68" viewBox="0 0 68 68" role="img" aria-label="Shield with hands holding a heart icon"><path d="M34 2 L66 12 L64 40 Q58 58 34 66 Q10 58 4 40 L2 12 Z" fill="#fff"/><path d="M34 10 L58 17 L56 39 Q51 53 34 59 Q17 53 12 39 L10 17 Z" fill="var(--brand-blue)" opacity=".15"/></svg>
      Healthcare
    </div>
    <div class="industry" style="left:259px;top:49px">
      <svg width="68" height="68" viewBox="0 0 68 68" role="img" aria-label="Shield with office buildings icon"><path d="M34 2 L66 12 L64 40 Q58 58 34 66 Q10 58 4 40 L2 12 Z" fill="#fff"/><path d="M34 10 L58 17 L56 39 Q51 53 34 59 Q17 53 12 39 L10 17 Z" fill="var(--brand-blue)" opacity=".15"/></svg>
      Real Estate
    </div>
    <div class="industry" style="left:353px;top:49px">
      <svg width="68" height="68" viewBox="0 0 68 68" role="img" aria-label="Shield with nuclear plant icon"><path d="M34 2 L66 12 L64 40 Q58 58 34 66 Q10 58 4 40 L2 12 Z" fill="#fff"/><path d="M34 10 L58 17 L56 39 Q51 53 34 59 Q17 53 12 39 L10 17 Z" fill="var(--brand-blue)" opacity=".15"/></svg>
      Nuclear
    </div>
    <div class="industry" style="left:447px;top:49px">
      <svg width="68" height="68" viewBox="0 0 68 68" role="img" aria-label="Shield with secure access device icon"><path d="M34 2 L66 12 L64 40 Q58 58 34 66 Q10 58 4 40 L2 12 Z" fill="#fff"/><path d="M34 10 L58 17 L56 39 Q51 53 34 59 Q17 53 12 39 L10 17 Z" fill="var(--brand-blue)" opacity=".15"/></svg>
      Highly secure<br>facilities
    </div>
  </div>

  <div class="certification">
    <h2 class="section-title" style="margin-bottom:9px">Accredited Defense Specialist (ADS)</h2>
    <p>The Accredited Defense Specialist (ADSⓇ) is considered the “gold standard” certification for security management professionals and demonstrates knowledge and competency in seven key domains of security. Globally recognized as the standard of excellence for security management professionals. The ADS is administered by OPRA Worldwide, which is the predominant international organization for security Internationally.</p>
  </div>
  <div class="cert-badge" style="left:389px;top:601px;width:114px;height:36px" role="img" aria-label="Certification badge"></div>

  <div class="contact-tab"><span>Contact us:</span></div>
  <div class="contact-bar">
    <div class="item phone">
      <svg width="13" height="13" viewBox="0 0 24 24" aria-hidden="true"><path d="M6.6 10.8a15 15 0 0 0 6.6 6.6l2.2-2.2a1 1 0 0 1 1-.25 11.4 11.4 0 0 0 3.6.57 1 1 0 0 1 1 1V20a1 1 0 0 1-1 1A17 17 0 0 1 3 4a1 1 0 0 1 1-1h3.5a1 1 0 0 1 1 1c0 1.25.2 2.45.57 3.57a1 1 0 0 1-.25 1z" fill="none" stroke="#fff" stroke-width="1.8"/></svg>
      555-271-6043
    </div>
    <span class="divider" style="left:161px"></span>
    <div class="item mail">
      <svg width="13" height="10" viewBox="0 0 26 20" aria-hidden="true"><rect x="1" y="1" width="24" height="18" fill="none" stroke="#fff" stroke-width="2"/><path d="M1 1 L13 11 L25 1" fill="none" stroke="#fff" stroke-width="2"/></svg>
      info@varnelguard.example
    </div>
    <span class="divider" style="left:329px"></span>
    <div class="item web">
      <svg width="13" height="13" viewBox="0 0 24 24" aria-hidden="true"><g fill="none" stroke="#fff" stroke-width="1.6"><circle cx="12" cy="12" r="10"/><ellipse cx="12" cy="12" rx="4.5" ry="10"/><path d="M2 12h20M4 6.5h16M4 17.5h16"/></g></svg>
      www.varnelguard.example
    </div>
  </div>
</section>

<!-- BACK PAGE -->
<section class="page page--back">
  <div class="brand" style="left:24px;top:44px;font-size:24px">
    <span class="brand__mark" style="width:22px;height:22px"></span>Varnel
  </div>
  <div class="cert-badge" style="left:336px;top:28px;width:140px;height:44px" role="img" aria-label="Certification badge"></div>

  <svg class="layer" width="519" height="360" viewBox="0 0 519 360">
    <defs>
      <linearGradient id="netGrad" x1="0" y1="0" x2="1" y2="0">
        <stop offset="0" stop-color="#2c3038"/>
        <stop offset=".45" stop-color="#5d6470"/>
        <stop offset=".8" stop-color="#2b3a55"/>
        <stop offset="1" stop-color="#1d2535"/>
      </linearGradient>
    </defs>
    <polygon points="0,120 154,120 187,87 519,87 519,93 190,93 157,126 0,126" fill="var(--brand-blue)"/>
    <polygon role="img" aria-label="Businessman touching a glowing padlock within a network of connected security nodes" points="0,128 158,128 191,96 519,96 519,310 380,310 350,340 0,340" fill="url(#netGrad)"/>
    <polygon points="0,344 352,344 382,314 519,314 519,320 386,320 356,350 0,350" fill="var(--slate)"/>
  </svg>

  <svg class="layer" style="top:370px" width="519" height="284" viewBox="0 0 519 284">
    <polygon points="0,0 296,0 220,284 0,284" fill="var(--charcoal)"/>
    <polygon points="300,0 305,0 229,284 224,284" fill="var(--brand-blue)"/>
    <polygon points="311,0 519,0 519,284 235,284" fill="var(--brand-blue)"/>
  </svg>

  <div class="panel-tab" style="left:18px;top:383px;width:92px">Who we are:</div>
  <ul class="shield-list who">
    <li>Over 25+ years of experience in Security and Law Enforcement</li>
    <li>Specialize in Security Management</li>
    <li>Board Certified in Security management</li>
    <li>Accredited defense Specialist (ADS)</li>
    <li>We are not affiliated with any security provider or guard company we provide independent advise</li>
  </ul>

  <div class="panel-tab" style="left:18px;top:518px;width:132px">Area's of Expertise:</div>
  <ul class="shield-list expertise">
    <li>Security Management</li>
    <li>Security Department Reorganization</li>
    <li>Physical Security</li>
    <li>Electronic Security</li>
    <li>Information Security</li>
    <li>Transportation Security</li>
    <li>Security in Highly Regulated environments</li>
  </ul>

  <div class="services-tab">Services Offered:</div>
  <div class="services">
    <div class="services__edge"></div>
    <ul>
      <li>Security Management</li>
      <li>Security Management Mentoring / Development</li>
      <li>Risk Assessments</li>
      <li>Security Risk Management</li>
      <li>Security Audits</li>
      <li>Security Performance Testing (Red Team)</li>
      <li>Threat Assessments</li>
      <li>Vulnerability Assessments</li>
      <li>Security Planning</li>
      <li>RFP/RFQ</li>
      <li>Project management</li>
      <li>Security Policy Development</li>
      <li>Security Program Review</li>
      <li>Security System Design Management</li>
      <li>High Risk Planning</li>
      <li>Litigation Planning and Consulting</li>
    </ul>
  </div>

  <div class="contact-tab"><span>Contact us:</span></div>
  <div class="contact-bar">
    <div class="item phone">
      <svg width="13" height="13" viewBox="0 0 24 24" aria-hidden="true"><path d="M6.6 10.8a15 15 0 0 0 6.6 6.6l2.2-2.2a1 1 0 0 1 1-.25 11.4 11.4 0 0 0 3.6.57 1 1 0 0 1 1 1V20a1 1 0 0 1-1 1A17 17 0 0 1 3 4a1 1 0 0 1 1-1h3.5a1 1 0 0 1 1 1c0 1.25.2 2.45.57 3.57a1 1 0 0 1-.25 1z" fill="none" stroke="#fff" stroke-width="1.8"/></svg>
      555-271-6043
    </div>
    <span class="divider" style="left:161px"></span>
    <div class="item mail">
      <svg width="13" height="10" viewBox="0 0 26 20" aria-hidden="true"><rect x="1" y="1" width="24" height="18" fill="none" stroke="#fff" stroke-width="2"/><path d="M1 1 L13 11 L25 1" fill="none" stroke="#fff" stroke-width="2"/></svg>
      info@varnelguard.example
    </div>
    <span class="divider" style="left:329px"></span>
    <div class="item web">
      <svg width="13" height="13" viewBox="0 0 24 24" aria-hidden="true"><g fill="none" stroke="#fff" stroke-width="1.6"><circle cx="12" cy="12" r="10"/><ellipse cx="12" cy="12" rx="4.5" ry="10"/><path d="M2 12h20M4 6.5h16M4 17.5h16"/></g></svg>
      www.varnelguard.example
    </div>
  </div>
</section>

</body>
</html>
```